Energy trading company (Voltrisa) needs a business card

We need a business card for a company based in Central America. Our main purpose is trading energy . We already have the logo but we need some good creativity to design a high impact business card. Colors blue, orange, green can be used or we would like to see good combinatios with our logo

Target Market(s)

Energy

Industry/Entity Type

Power Generation

Contact Information for Business Card

Logo , headquarters , name, background

Font styles to use
Serif
Sans Serif

Colors

Designer to choose colors to be used in the design.

Requirements
Must have
• it must have a fresh and clean view
Nice to have
• good backgrounds that combine with the logo
Should not have
• too much words

```html
<!DOCTYPE html>
<html lang="en">
<head>
<meta charset="UTF-8">
<title>Voltrisa Business Card</title>
<link rel="stylesheet" href="https://fonts.googleapis.com/css2?family=Montserrat:wght@400;500;700&display=swap">
<style>
  :root {
    --backdrop: #e4e4e4;
    --card: #1d1c1c;
    --accent: #f7941d;
    --text-light: #e8e8e8;
    --text-muted: #bdbdbd;
  }
  * { margin: 0; padding: 0; box-sizing: border-box; }
  html, body {
    width: 1200px; height: 1200px; overflow: hidden;
    background: var(--backdrop);
    font-family: "Montserrat", Arial, sans-serif;
  }
  .canvas {
    width: 1200px; height: 1200px;
    display: flex; flex-direction: column; align-items: center; justify-content: center;
    gap: 52px;
  }
  .card {
    width: 900px; height: 514px;
    background: var(--card);
    border: 5px solid var(--accent);
    position: relative;
    box-shadow: 0 10px 30px rgba(0,0,0,0.18);
  }
  /* Back: contact side */
  .card--contact { display: flex; align-items: center; }
  .brand-block {
    width: 420px;
    display: flex; flex-direction: column; align-items: center; justify-content: center;
    gap: 22px;
  }
  .brand-mark {
    width: 92px; height: 92px; border-radius: 50%;
    background: var(--accent);
  }
  .brand-name {
    color: var(--accent);
    font-weight: 500;
    font-size: 64px;
    letter-spacing: 1px;
    text-transform: uppercase;
    line-height: 1;
  }
  .divider {
    width: 3px; height: 330px; background: var(--accent);
  }
  .contact-block {
    padding-left: 44px;
    color: var(--text-light);
  }
  .person-name {
    color: var(--accent); font-weight: 700; font-size: 32px;
    letter-spacing: 1px; text-transform: uppercase;
  }
  .person-title { font-size: 19px; color: var(--text-muted); margin-top: 4px; }
  .address {
    font-size: 17px; line-height: 1.5; margin-top: 28px; max-width: 370px;
  }
  .contact-list { list-style: none; margin-top: 22px; }
  .contact-list li {
    display: flex; align-items: center; gap: 14px;
    font-size: 17px; line-height: 1.9;
  }
  .contact-list svg { width: 18px; height: 18px; flex-shrink: 0; }

  /* Front: brand side */
  .card--brand {
    display: flex; flex-direction: column; align-items: center; justify-content: center;
    gap: 34px;
  }
  .card--brand .brand-mark { width: 150px; height: 150px; }
  .card--brand .brand-name { font-size: 104px; }
</style>
</head>
<body>
<main class="canvas">
  <section class="card card--contact">
    <div class="brand-block">
      <div class="brand-mark"></div>
      <div class="brand-name">Voltrisa</div>
    </div>
    <div class="divider"></div>
    <div class="contact-block">
      <h1 class="person-name">Lucas Moreno</h1>
      <p class="person-title">President</p>
      <p class="address">00000 Main St Ste 201, Central America, WA 00000</p>
      <ul class="contact-list">
        <li>
          <svg viewBox="0 0 24 24" aria-hidden="true"><path fill="#f7941d" d="M6.6 10.8a15.1 15.1 0 0 0 6.6 6.6l2.2-2.2a1 1 0 0 1 1-.25 11.4 11.4 0 0 0 3.6.57 1 1 0 0 1 1 1V20a1 1 0 0 1-1 1A17 17 0 0 1 3 4a1 1 0 0 1 1-1h3.5a1 1 0 0 1 1 1c0 1.25.2 2.45.57 3.57a1 1 0 0 1-.25 1z"/></svg>
          <span>+00 000 000 000</span>
        </li>
        <li>
          <svg viewBox="0 0 24 24" aria-hidden="true"><rect x="2" y="5" width="20" height="14" rx="1.5" fill="none" stroke="#f7941d" stroke-width="2"/><path d="M3 6l9 7 9-7" fill="none" stroke="#f7941d" stroke-width="2"/></svg>
          <span>info@voltrisa.com</span>
        </li>
        <li>
          <svg viewBox="0 0 24 24" aria-hidden="true"><circle cx="12" cy="12" r="9.5" fill="none" stroke="#f7941d" stroke-width="2"/><path d="M2.5 12h19M12 2.5c3 3 3 16 0 19M12 2.5c-3 3-3 16 0 19" fill="none" stroke="#f7941d" stroke-width="1.6"/></svg>
          <span>www.voltrisa.com</span>
        </li>
      </ul>
    </div>
  </section>

  <section class="card card--brand">
    <div class="brand-mark"></div>
    <div class="brand-name">Voltrisa</div>
  </section>
</main>
</body>
</html>
```